Update KORVEN Global's Website

We need to update our current website - www.korvenglobal.example, either with the same template (Joomla 1.5 CMS site using the Plumtrack Meridian) or new one. Please see the first Attached File for additional details of the changes we would like.

A brief summary of changes are:
- Change colors and update the tagline on the logo
- Remove text and add text and pictures
- Remove pages and add a page
and other minor changes

The site is currently hosted at Ta Welbo. You will have access to the FTP file transfer to download and work with the current files.

Please contact me with any questions: derek@korvenglobal.example
Updates

Project Deadline Extended
Reason: Extending to view additional designs. Please indicate if you are proposing a completely new site or redo of the current template. Best, Derek

```html
<!DOCTYPE html>
<html lang="en">
<head>
<meta charset="utf-8">
<title>KORVEN Global – Bioenergy &amp; Social Investments</title>
<link href="https://fonts.googleapis.com/css2?family=Roboto:ital,wght@0,400;0,500;0,700;1,300&family=Oswald:wght@400&display=swap" rel="stylesheet">
<style>
:root{
  --blue:#3a86cc;
  --blue-dark:#2f74b8;
  --nav-top:#5aa1dc;
  --nav-bottom:#3d88cc;
  --orange:#f9ab2e;
  --text:#555;
  --text-dark:#222;
  --grey:#888;
  --footer:#0f2640;
  --white:#fff;
}
*{margin:0;padding:0;box-sizing:border-box}
html,body{width:1184px;height:1200px;overflow:hidden;background:var(--white)}
body{position:relative;font-family:'Roboto',sans-serif;color:var(--text)}
.abs{position:absolute}
.top-strip{left:0;top:0;width:1184px;height:8px;background:var(--blue)}
.brand{left:198px;top:28px;display:flex;align-items:center;gap:8px}
.brand-mark{width:26px;height:26px;border-radius:50%;background:var(--orange)}
.brand-name{font-size:29px;font-weight:500;color:var(--blue);line-height:1}
.tagline{left:236px;top:57px;font-size:15px;font-style:italic;font-weight:300;color:#999}
.search{left:594px;top:34px;width:152px;height:21px;border:1px solid #ddd;font-size:9px;color:#999;padding:5px 6px}
.search-btn{left:746px;top:34px;width:22px;height:21px;background:#333}
.social-top{left:769px;top:34px;display:flex;gap:1px}
.social-top span{width:22px;height:21px;display:block}
.lang{left:898px;top:32px;width:89px;height:24px;border:1px solid #ccc;border-radius:2px;background:#f7f7f7;font-size:10px;color:var(--text-dark);display:flex;align-items:center}
.lang .flag{width:15px;height:10px;background:#b5bcc9;margin:0 5px 0 6px}
.lang .caret{margin-left:auto;width:20px;height:100%;border-left:1px solid #ccc;display:flex;align-items:center;justify-content:center}
.contact-line{left:676px;top:64px;font-size:9.5px;color:var(--grey);display:flex;gap:12px;align-items:center}
.contact-line span{display:flex;align-items:center;gap:5px}
.nav{left:0;top:83px;width:1184px;height:50px;background:linear-gradient(var(--nav-top),var(--nav-bottom))}
.nav a{position:absolute;top:0;height:50px;line-height:50px;text-align:center;color:var(--white);font-size:10.5px;text-decoration:none;border-right:1px solid rgba(0,0,0,.12)}
.nav a.active{background:var(--orange);border-right:none}
.hero{left:0;top:133px;width:1184px;height:445px;background:linear-gradient(180deg,#7fb2e4 0%,#b7d4ee 35%,#b9a37b 55%,#8b7a5a 75%,#6c8c3e 90%,#7aa04a 100%)}
.arrow{top:313px;width:49px;height:54px;background:rgba(30,30,30,.85);display:flex;align-items:center;justify-content:center}
.dots{left:582px;top:547px;display:flex;gap:6px}
.dots i{width:11px;height:11px;border-radius:50%;border:2px solid var(--white);background:transparent;display:block}
.dots i.on{background:var(--blue)}
.welcome-title{left:198px;top:605px;font-size:19.5px;color:var(--blue);font-weight:400}
.welcome-text{left:198px;top:640px;width:490px;font-size:9.8px;line-height:14.2px;color:var(--text)}
.welcome-text p{margin-bottom:6.5px}
.feature{left:700px;top:608px;width:287px;height:172px;background:linear-gradient(160deg,#4f5a3c,#7b7a62 50%,#3e4a2c);border:1px solid #ccc;display:flex;align-items:center;justify-content:center}
.feature span{font-family:'Oswald',sans-serif;font-size:20px;color:var(--white)}
.card-img{top:818px;height:160px;width:245px;border:1px solid #ddd}
.card-title{top:990px;font-size:14.5px;color:var(--blue)}
.card-text{top:1016px;font-size:9.8px;line-height:19px;color:var(--text);width:250px}
.spec{display:grid;grid-template-columns:57px 1fr;row-gap:5px;font-size:9.6px;line-height:12.5px}
.spec b{font-weight:500;color:var(--text-dark)}
.offices-title{left:740px;top:915px;font-size:14.5px;color:var(--blue)}
.offices{left:740px;top:936px;width:240px;font-size:9.6px;line-height:14.1px;color:var(--text)}
.offices strong{font-weight:500;color:var(--text-dark)}
.offices hr{border:none;border-top:1px solid #ddd;margin:4px 0 5px}
.footer{left:0;top:1114px;width:1184px;height:86px;background:var(--footer)}
.footer-links{left:198px;top:1140px;font-size:9.8px;color:var(--white)}
.copyright{left:198px;top:1168px;font-size:9.8px;color:var(--white)}
.social-foot{left:879px;top:1146px;display:flex;gap:3px}
.social-foot span{width:25px;height:25px;display:block}
</style>
</head>
<body>
<div class="abs top-strip"></div>

<div class="abs brand"><span class="brand-mark"></span><span class="brand-name">KORVEN Global</span></div>
<div class="abs tagline">Bioenergy &amp; Social Investments</div>

<div class="abs search">Search ...</div>
<div class="abs search-btn" aria-label="Search">
  <svg width="22" height="21" viewBox="0 0 22 21"><circle cx="10" cy="9.5" r="3.5" fill="none" stroke="#fff" stroke-width="1.6"/><line x1="12.6" y1="12" x2="15" y2="14.5" stroke="#fff" stroke-width="1.8"/></svg>
</div>
<div class="abs social-top" aria-label="Social links">
  <span style="background:#39a8de"></span><span style="background:#3b5b9a"></span><span style="background:#e2508a"></span><span style="background:#1475b0"></span><span style="background:#f5a623"></span>
</div>
<div class="abs lang"><span class="flag"></span>English<span class="caret"><svg width="6" height="4"><path d="M0 0h6L3 4z" fill="#777"/></svg></span></div>

<div class="abs contact-line">
  <span><svg width="8" height="8" viewBox="0 0 8 8"><path d="M1 0.5l1.6 0 .6 1.8-1 .8a4.5 4.5 0 0 0 2.6 2.6l.8-1 1.8.6v1.6a1 1 0 0 1-1 1A7 7 0 0 1 0 1.5a1 1 0 0 1 1-1z" fill="#888"/></svg>5550 1842</span>
  <span><svg width="9" height="7" viewBox="0 0 9 7"><rect width="9" height="7" fill="#888"/><path d="M0 0l4.5 3.5L9 0" fill="none" stroke="#fff" stroke-width=".8"/></svg>admin@korvenglobal.example</span>
</div>

<nav class="abs nav">
  <a class="active" style="left:198px;width:130px">Home</a>
  <a style="left:328px;width:168px">Community Development</a>
  <a style="left:496px;width:177px">Affordable Housing</a>
  <a style="left:673px;width:144px">Alternative Energy</a>
  <a style="left:817px;width:140px;border-right:none">KORVEN Team</a>
</nav>

<div class="abs hero" role="img" aria-label="Photo of a two-storey suburban family house with lawn and trees under a blue sky"></div>
<div class="abs arrow" style="left:0"><svg width="16" height="22"><path d="M12 2L4 11l8 9" fill="none" stroke="#fff" stroke-width="4"/></svg></div>
<div class="abs arrow" style="left:1139px;width:45px"><svg width="16" height="22"><path d="M4 2l8 9-8 9" fill="none" stroke="#fff" stroke-width="4"/></svg></div>
<div class="abs dots"><i class="on"></i><i></i><i></i></div>

<h1 class="abs welcome-title">Welcome To KORVEN Global</h1>
<div class="abs welcome-text">
  <p>KORVEN is a socially responsible corporation working in the areas of affordable housing and alternative energy.</p>
  <p>We at KORVEN think environmental and social accountability are as fundamental as making a profit. In fact, they go hand in hand. All our wide-ranging projects—from the development of affordable green housing to an island eco-lodge and residences—specialize in superior investment and ownership opportunities and employ the latest in sustainable and green technologies.</p>
  <p>Our vision is to create and support eco-friendly, sustainable property developments in Panama that maximize profit for our investors and strengthen communities for our neighbors.</p>
  <p>KORVEN Global: the next generation of sustainable real estate development in Panama.</p>
</div>
<div class="abs feature" role="img" aria-label="Photo of a stone house behind a large tree"><span>Affordable Green Housing</span></div>

<div class="abs card-img" style="left:198px;background:linear-gradient(180deg,#cfe3f2 0%,#5d8a3a 40%,#7fb04c 75%,#a9c96a 100%)" role="img" aria-label="Photo of a curving footpath through green lawns and trees"></div>
<div class="abs card-title" style="left:196px">Green Communities Space</div>
<div class="abs card-text" style="left:198px">Lorem ipsum dolor sit amet, consectetuer adipiscing elit, sed diam nonummy nibh euismod tincidunt ut laoreet dolore magna aliquam erat volutpat.</div>

<div class="abs card-img" style="left:470px;background:linear-gradient(180deg,#4f87c9 0%,#9cc3e6 35%,#6f8f3c 55%,#4e6a2c 80%,#3a4c32 100%)" role="img" aria-label="Photo of a modern house with green planted roofs"></div>
<div class="abs card-title" style="left:470px">Community Development</div>
<div class="abs card-text spec" style="left:471px;top:1019px;width:240px">
  <b>Type :</b><span>Master Planned Single Family</span>
  <b>Size :</b><span>600 units at build-out</span>
  <b>Amenities:</b><span>State-of-the-art community with swim center and shady parks.</span>
</div>

<div class="abs card-img" style="left:740px;height:86px;background:linear-gradient(90deg,#e8e4da 0%,#efe9df 60%,#a3c4f2 72%,#9cbff0 100%)" role="img" aria-label="Street map of Panama City"></div>
<div class="abs offices-title">Offices :</div>
<div class="abs offices">
  <strong>KORVEN Panama, S.A.</strong><br>
  Panama Office<br>
  Las Brisas, Plaza Comercial Ventura, #22<br>
  Panama City, Panama<br>
  Ofc: 507-555-0148 Fax: 507-555-0193<br>
  contact@korvenglobal.example
  <hr>
  <strong>U.S. Office</strong><br>
  410-12th Ave North, #305<br>
  Lakeport, WA 98000<br>
  Ofc: 202-555-0172 Fax: 703-555-0126
</div>

<footer class="abs footer"></footer>
<div class="abs footer-links">Home | About | Practices | People | Events | Contact | Site Map | Privacy Policy</div>
<div class="abs copyright">Copyright © 2014 KORVEN Global. All Rights Reserved</div>
<div class="abs social-foot" aria-label="Social links">
  <span style="background:#3b5b9a"></span><span style="background:#39a8de"></span><span style="background:#dd4b39"></span><span style="background:#1475b0"></span>
</div>
</body>
</html>
```